Bottlecap Decals Inc. NEED DESIGNS FOR THE HOLIDAY STICKERS

We need 6 designs for the HOLIDAY SET of Bottlecap Decals. I have attached some imagery that we like as well as the flagship pack of stickers that were also designed by you AWESOME DESIGNERS!! You are not limited to this imagery, it is only to show you what style we like but remember, YOU ARE THE ARTIST! Each design needs to have a "TO: & FROM:" for people to write in their name and the recipients name. We need designs for the following occasions:

1. HALLOWEEN
2. HAPPY HOLIDAYS (THANKSGIVING, CHRISTMAS, WINTER, LEAVES)
3. ST. PATRICK'S DAY
4. "LET'S CELEBRATE" PATRIOTIC THEME (JULY 4TH, VETERANS DAY, MEMORIAL DAY COMBINED)
5. HAPPY NEW YEAR
6. SUMMER THEME GENERIC

***these 6 designs must fit on one of die cut shapes which are included in the brief***

**PLEASE SUBMIT YOUR IDEA FOR AS MANY DESIGNS AS YOU CAN (PREFERABLY ALL 6). WE NEED 6 DESIGNS SO IF 4 OF YOURS ARE GOOD AND 2 OF ANOTHERS ARE GOOD, YOU WOULD WIN 1ST AND THEY WOULD WIN 2ND.

Font styles to use
Serif
Sans Serif
Decorative
Script

Requirements
Must have
• - lines for "to" and "from"
• - must fit on a die cut shape (provided)
• - must be FUN and colorful!!
Nice to have
• color, imagery, fun!

```html
<!DOCTYPE html>
<html lang="en">
<head>
<meta charset="utf-8">
<title>Let's Celebrate – Holiday Sticker</title>
<link rel="stylesheet" href="https://fonts.googleapis.com/css2?family=Russo+One&family=Montserrat:wght@500;600&display=swap">
<style>
  :root {
    --navy: #232a5c;
    --flag-blue: #2f5fb3;
    --flag-red: #c8252f;
    --band-red: #c0222c;
    --banner-red: #a61e27;
    --cream: #f6f1df;
    --blush: #f3cdbf;
    --white: #ffffff;
    --page: #e9e6e0;
  }
  html, body {
    margin: 0;
    padding: 0;
    width: 1200px;
    height: 1200px;
    overflow: hidden;
    background: var(--page);
  }
  .canvas {
    position: relative;
    width: 1200px;
    height: 1200px;
  }
  .sticker {
    position: absolute;
    left: 220px;
    top: 100px;
    width: 760px;
    height: 1000px;
  }
  .sticker-shape {
    position: absolute;
    inset: 0;
    width: 760px;
    height: 1000px;
    overflow: visible;
  }
  .headline {
    position: absolute;
    left: 0;
    top: 300px;
    width: 760px;
    text-align: center;
  }
  .headline-small {
    display: inline-block;
    font-family: "Russo One", sans-serif;
    font-size: 56px;
    line-height: 1;
    color: var(--white);
    background: var(--navy);
    padding: 8px 20px 6px;
    margin-left: -160px;
    text-shadow: 0 3px 0 #9aa3b8;
    letter-spacing: 1px;
  }
  .headline-banner {
    margin: 4px auto 0;
    width: 660px;
    background: linear-gradient(180deg, #c42a33 0%, var(--banner-red) 100%);
    box-shadow: 0 6px 10px rgba(80, 10, 15, 0.35);
  }
  .headline-large {
    display: block;
    font-family: "Russo One", sans-serif;
    font-size: 106px;
    line-height: 1.05;
    color: var(--white);
    letter-spacing: 2px;
    text-shadow: 0 2px 0 #d7dbe3, 0 5px 0 #8f95a6, 0 8px 8px rgba(0,0,0,0.35);
  }
  .address {
    position: absolute;
    left: 80px;
    top: 690px;
    width: 600px;
    font-family: "Montserrat", sans-serif;
    color: var(--navy);
  }
  .address-row {
    margin-bottom: 26px;
  }
  .address-label {
    display: block;
    text-align: center;
    font-size: 36px;
    font-weight: 600;
    letter-spacing: 1px;
    margin-bottom: 10px;
  }
  .address-line {
    display: block;
    height: 0;
    border-bottom: 4px dotted var(--navy);
  }
</style>
</head>
<body>
<main class="canvas">
  <div class="sticker">
    <svg class="sticker-shape" viewBox="0 0 760 1000" xmlns="http://www.w3.org/2000/svg">
      <defs>
        <clipPath id="label-clip">
          <path d="M0 300 L0 950 A50 50 0 0 1 50 1000 L710 1000 A50 50 0 0 1 760 950 L760 300 A50 50 0 0 1 710 250 C650 -20 110 -20 50 250 A50 50 0 0 1 0 300 Z"/>
        </clipPath>
        <linearGradient id="flag-tones" x1="0" y1="0" x2="0" y2="1">
          <stop offset="0" stop-color="#2f5fb3"/>
          <stop offset="0.38" stop-color="#3b6cc0"/>
          <stop offset="0.55" stop-color="#d9a3a3"/>
          <stop offset="0.75" stop-color="#c8252f"/>
          <stop offset="1" stop-color="#d4535a"/>
        </linearGradient>
        <linearGradient id="cream-tones" x1="0" y1="0" x2="0" y2="1">
          <stop offset="0" stop-color="#f3cdbf"/>
          <stop offset="0.45" stop-color="#f6e6d8"/>
          <stop offset="1" stop-color="#f6f1df"/>
        </linearGradient>
      </defs>
      <g clip-path="url(#label-clip)">
        <rect class="flag-art" x="0" y="0" width="760" height="620" fill="url(#flag-tones)" role="img" aria-label="Waving watercolour American flag with stars and bursting fireworks"/>
        <rect class="lower-field" x="0" y="620" width="760" height="380" fill="url(#cream-tones)" role="img" aria-label="Faded red and cream flag stripes behind the writing area"/>
        <rect class="red-band" x="0" y="560" width="760" height="60" fill="var(--band-red)"/>
      </g>
      <path d="M0 300 L0 950 A50 50 0 0 1 50 1000 L710 1000 A50 50 0 0 1 760 950 L760 300 A50 50 0 0 1 710 250 C650 -20 110 -20 50 250 A50 50 0 0 1 0 300 Z" fill="none" stroke="var(--navy)" stroke-width="6"/>
    </svg>

    <div class="headline">
      <span class="headline-small">LET'S</span>
      <div class="headline-banner">
        <span class="headline-large">CELEBRATE</span>
      </div>
    </div>

    <div class="address">
      <div class="address-row">
        <span class="address-label">TO</span>
        <span class="address-line"></span>
      </div>
      <div class="address-row">
        <span class="address-label">FROM</span>
        <span class="address-line"></span>
      </div>
    </div>
  </div>
</main>
</body>
</html>
```